Business Card Design

We are a General Practice - Family medicine
We also have Allied Health professionals working within our team

Industry/Entity Type

Business

Contact Information for Business Card

Front of the card to display:

BRAMBLEWICK MEDICAL
PHONE 6348 2917

5/41 Fennimore Parade
Launceston Tasmania 7284

Back of the card to display:

My Appointments
Date:
Time:
With:

Please remember to phone us on 6348 2917 to cancel your appointment if you can't keep it.
A fee applied to missed appointments

```html
<!DOCTYPE html>
<html lang="en">
<head>
<meta charset="utf-8">
<title>Bramblewick Medical – Business Card</title>
<link rel="stylesheet" href="https://fonts.googleapis.com/css2?family=Didact+Gothic&display=swap">
<style>
  :root {
    --backdrop: #e9e7e4;
    --card: #ffffff;
    --ink: #333333;
    --brand-blue: #2b9fd9;
    --brand-green: #7cbf3f;
    --panel-green: #d3e9b2;
    --panel-blue: #addcf1;
    --rule: #d9d9d9;
    --mark-tint: #e4f0f7;
  }
  * { box-sizing: border-box; margin: 0; padding: 0; }
  html, body { width: 1200px; height: 800px; overflow: hidden; }
  body {
    background: var(--backdrop);
    font-family: "Didact Gothic", "Century Gothic", sans-serif;
    color: var(--ink);
    display: flex;
    align-items: center;
    justify-content: center;
    gap: 60px;
  }
  .card {
    width: 520px;
    height: 297px;
    background: var(--card);
    position: relative;
    overflow: hidden;
    box-shadow: 0 2px 10px rgba(0,0,0,0.12);
  }

  /* Appointment side */
  .appointment { padding: 34px 36px 0; }
  .appointment__mark {
    position: absolute;
    left: 200px; top: 20px;
    width: 170px; height: 170px;
    border-radius: 50%;
    background: var(--mark-tint);
    opacity: 0.7;
  }
  .appointment__title { position: relative; font-size: 19px; margin-bottom: 14px; }
  .appointment__fields { position: relative; list-style: none; }
  .appointment__fields li { font-size: 19px; margin: 0 0 14px 10px; }
  .appointment__rule {
    position: relative;
    border: 0;
    border-top: 1px solid var(--rule);
    margin: 6px 0 10px;
  }
  .appointment__note {
    position: relative;
    text-align: center;
    font-size: 14px;
    line-height: 1.4;
    color: var(--brand-blue);
  }
  .appointment__fee { color: var(--brand-green); display: block; }

  /* Contact side */
  .contact { display: flex; }
  .contact__brand {
    width: 47%;
    display: flex;
    align-items: center;
    justify-content: center;
    border-right: 2px solid var(--brand-blue);
  }
  .contact__name { font-size: 25px; color: var(--brand-blue); text-align: center; line-height: 1.2; }
  .contact__details { flex: 1; display: flex; flex-direction: column; }
  .contact__panel {
    display: flex;
    flex-direction: column;
    align-items: center;
    justify-content: center;
    gap: 12px;
    text-align: center;
    font-size: 17px;
    line-height: 1.35;
  }
  .contact__panel--phone { background: var(--panel-green); height: 42%; }
  .contact__panel--address { background: var(--panel-blue); flex: 1; }
  .icon { width: 40px; height: 40px; }
</style>
</head>
<body>

  <section class="card appointment" aria-label="Appointment card">
    <div class="appointment__mark" aria-hidden="true"></div>
    <h2 class="appointment__title">My Appointments</h2>
    <ul class="appointment__fields">
      <li>Date:</li>
      <li>Time:</li>
      <li>With:</li>
    </ul>
    <hr class="appointment__rule">
    <p class="appointment__note">
      Please remember to phone us on 6348 2917 to cancel your<br>
      appointment if you can't keep it.
      <span class="appointment__fee">A fee applied to missed appointments.</span>
    </p>
  </section>

  <section class="card contact" aria-label="Contact card">
    <div class="contact__brand">
      <p class="contact__name">Bramblewick<br>Medical</p>
    </div>
    <div class="contact__details">
      <div class="contact__panel contact__panel--phone">
        <svg class="icon" viewBox="0 0 40 40" aria-hidden="true">
          <polygon points="20,2 36,11 36,29 20,38 4,29 4,11" fill="#fff" stroke="#333" stroke-width="2"/>
          <rect x="13" y="13" width="14" height="14" rx="2" fill="#2b9fd9"/>
          <rect x="16" y="15" width="3" height="10" fill="#fff"/>
          <rect x="21" y="16" width="4" height="2" fill="#fff"/>
          <rect x="21" y="20" width="4" height="2" fill="#fff"/>
        </svg>
        <span>6348 2917</span>
      </div>
      <div class="contact__panel contact__panel--address">
        <svg class="icon" viewBox="0 0 40 40" aria-hidden="true">
          <polygon points="20,2 36,11 36,29 20,38 4,29 4,11" fill="#fff" stroke="#333" stroke-width="2"/>
          <rect x="14" y="12" width="12" height="16" fill="#7cbf3f"/>
          <rect x="16" y="14" width="3" height="3" fill="#fff"/>
          <rect x="21" y="14" width="3" height="3" fill="#fff"/>
          <rect x="16" y="19" width="3" height="3" fill="#fff"/>
          <rect x="21" y="19" width="3" height="3" fill="#fff"/>
          <rect x="18.5" y="24" width="3" height="4" fill="#fff"/>
        </svg>
        <address style="font-style:normal">5/41 Fennimore Parade<br>Launceston Tasmania 7284</address>
      </div>
    </div>
  </section>

</body>
</html>
```